Stationary & Business Cards
Brimford Holdings
Project: Stationary & Business Cards
Stationary & Business Cards - Construction
Creative Brief
Simple
Dale Purcott
General Manager
P.O. Box 382 Ashbury CT 06218
Dale@BrimfordHoldings.com
ON THE STATIONARY ONLY: add our website www.BrimfordHoldings.com
logo to fill in entire back of business card. (Red background with blue lettering)

```html
<!DOCTYPE html>
<html lang="en">
<head>
<meta charset="utf-8">
<title>Brimford Holdings – Business Cards</title>
<link rel="stylesheet" href="https://fonts.googleapis.com/css2?family=Montserrat:wght@400;600;800&display=swap">
<style>
  :root {
    --bg: #e9e7e3;
    --brand-red: #d3283a;
    --brand-blue: #1d3f7a;
    --ink: #3a3a3a;
    --ink-soft: #6b6b6b;
    --card-white: #f7f7f7;
    --rule: #c9c9c9;
  }
  * { margin: 0; padding: 0; box-sizing: border-box; }
  html, body { width: 1200px; height: 904px; overflow: hidden; }
  body {
    background: var(--bg);
    font-family: "Montserrat", Arial, sans-serif;
    position: relative;
  }
  .card {
    position: absolute;
    width: 560px;
    height: 320px;
    border-radius: 4px;
    box-shadow: 0 10px 26px rgba(0,0,0,0.18);
    overflow: hidden;
  }
  .card-back {
    left: 90px;
    top: 110px;
    background: var(--brand-red);
    display: flex;
    align-items: center;
    justify-content: center;
  }
  .wordmark {
    color: var(--brand-blue);
    font-weight: 800;
    text-transform: uppercase;
    letter-spacing: 1px;
    line-height: 1;
    white-space: nowrap;
    display: flex;
    align-items: center;
    gap: 10px;
  }
  .wordmark-dot {
    width: 12px; height: 12px;
    background: var(--brand-blue);
    border-radius: 50%;
    flex: none;
  }
  .card-back .wordmark { font-size: 34px; }
  .card-front {
    left: 550px;
    top: 470px;
    background: var(--card-white);
  }
  .front-band {
    position: absolute;
    left: 0; right: 0; bottom: 0;
    height: 44px;
    background: var(--brand-red);
  }
  .card-front .wordmark {
    position: absolute;
    left: 30px;
    top: 153px;
    width: 250px;
    font-size: 16px;
    letter-spacing: 0.5px;
    gap: 8px;
  }
  .card-front .wordmark-dot { width: 8px; height: 8px; }
  .contact {
    position: absolute;
    left: 300px;
    top: 48px;
    padding-left: 18px;
    border-left: 1px solid var(--rule);
    color: var(--ink);
    font-size: 12px;
    line-height: 1.45;
  }
  .contact-name { color: var(--brand-blue); font-weight: 600; font-size: 15px; }
  .contact-title { color: var(--ink-soft); font-size: 11.5px; margin-bottom: 16px; }
  .contact-address { margin-bottom: 16px; }
  .contact-line { display: flex; align-items: center; gap: 8px; }
  .contact-line svg { width: 12px; height: 12px; flex: none; fill: var(--brand-red); }
</style>
</head>
<body>
  <section class="card card-back" aria-label="Business card back">
    <div class="wordmark"><span class="wordmark-dot"></span>Brimford Holdings</div>
  </section>

  <section class="card card-front" aria-label="Business card front">
    <div class="wordmark"><span class="wordmark-dot"></span>Brimford Holdings</div>

    <div class="contact">
      <p class="contact-name">Dale Purcott</p>
      <p class="contact-title">General Manager</p>
      <p class="contact-address">P.O. Box 382<br>Ashbury CT 06218</p>
      <p class="contact-line">
        <svg viewBox="0 0 24 24" aria-hidden="true"><path d="M6.6 10.8a15.1 15.1 0 0 0 6.6 6.6l2.2-2.2a1 1 0 0 1 1-.25 11.4 11.4 0 0 0 3.6.57 1 1 0 0 1 1 1V20a1 1 0 0 1-1 1A17 17 0 0 1 3 4a1 1 0 0 1 1-1h3.5a1 1 0 0 1 1 1c0 1.25.2 2.45.57 3.6a1 1 0 0 1-.25 1z"/></svg>
        860-555-0172
      </p>
      <p class="contact-line">
        <svg viewBox="0 0 24 24" aria-hidden="true"><rect x="6" y="1" width="12" height="22" rx="2"/></svg>
        860-555-0198
      </p>
      <p class="contact-line">
        <svg viewBox="0 0 24 24" aria-hidden="true"><path d="M2 5h20v14H2z M2 5l10 8 10-8" stroke="#fff" stroke-width="1.5"/></svg>
        Dale@BrimfordHoldings.com
      </p>
    </div>

    <div class="front-band"></div>
  </section>
</body>
</html>
```